Bref créative
Stationary Pack
Business Cards, Letterheads, fax etc
Professional
Luc-Henri Dorsay, MEE, MBME, MHIT, MBHA, ID-Ph.D
Senior Executive Consultant
9 Brindle Way, Suite 305
Toronto ON K7R4B9
Canada
luc-henri.dorsay@vextorian.example
www.vextorian.example
We require the following in our pack: Business cards, fax cover sheets, letterheads, envelopes, CD cases & labels, Email signatures,
Business Consulting and Professional Services Portfolio:
- eHealth consulting and research
- Healthcare IT project management
- Biomedical and health informatics
- Hospital and clinical engineering
- Business analysis and management
- Clean energy and technology management
- eLearning and knowledge translation

```html
<!DOCTYPE html>
<html lang="en">
<head>
<meta charset="utf-8">
<title>Vextorian Stationery Pack</title>
<link href="https://fonts.googleapis.com/css2?family=Open+Sans:wght@400;600;700&display=swap" rel="stylesheet">
<style>
:root{
  --bg:#e8e5e0;
  --paper:#ffffff;
  --brand-blue:#2d6cc0;
  --brand-blue-dark:#1f56a3;
  --accent-green:#7dbb3c;
  --ink:#3a3a3a;
  --ink-soft:#8a8a8a;
  --rule:#d4d4d4;
  --shadow:0 2px 6px rgba(0,0,0,.18);
}
*{box-sizing:border-box;margin:0;padding:0}
html,body{width:1200px;height:823px;overflow:hidden}
body{background:var(--bg);font-family:"Open Sans",Arial,sans-serif;color:var(--ink);position:relative}
.piece{position:absolute;background:var(--paper);box-shadow:var(--shadow);overflow:hidden}
.logo{display:flex;align-items:center;gap:5px}
.logo-dot{width:9px;height:9px;border-radius:50%;background:var(--accent-green);flex:none}
.logo-name{font-weight:700;color:var(--brand-blue);letter-spacing:.06em;font-size:13px}
.logo.on-blue .logo-name{color:#fff}
.logo.small .logo-name{font-size:9px}
.logo.small .logo-dot{width:6px;height:6px}
.fine{font-size:5px;line-height:7px;color:var(--ink-soft)}
.name{font-size:6px;font-weight:700;color:var(--ink)}

/* business cards, top */
.card-front{left:336px;top:46px;width:264px;height:132px;padding:14px}
.card-front .contact{position:absolute;right:14px;top:52px;text-align:left}
.card-front .addr{position:absolute;left:14px;top:60px}
.card-front .web{position:absolute;left:0;right:0;bottom:6px;text-align:center}
.card-list{left:504px;top:40px;width:128px;height:130px;padding:14px 10px}
.card-list .line{height:4px;background:var(--rule);margin:6px 0;width:80%}
.card-blue{left:590px;top:82px;width:176px;height:112px;background:var(--brand-blue);padding:10px 12px;color:#fff}
.card-blue .heading{font-size:5px;font-weight:700;margin-bottom:4px}
.card-blue li{font-size:4.6px;line-height:7px;list-style:none}
.card-blue li::before{content:"• "}
.card-blue .logo{position:absolute;right:12px;bottom:18px}

/* envelopes */
.envelope{width:280px;height:124px}
.envelope .flap{position:absolute;left:0;top:0;width:100%;height:36px;background:var(--brand-blue)}
.envelope .window{position:absolute;left:110px;top:60px;width:110px;height:34px;border:1px solid var(--rule)}
.env-back{left:870px;top:84px}
.env-front{left:872px;top:118px}
.env-front .logo{position:absolute;left:14px;top:44px}

/* letterhead and fax */
.sheet{width:290px;height:372px;padding:22px 26px}
.letterhead{left:144px;top:216px}
.fax{left:470px;top:216px}
.sheet-foot{position:absolute;left:0;right:0;bottom:10px;text-align:center}
.sheet-rule{position:absolute;left:26px;right:26px;bottom:26px;height:1px;background:var(--accent-green)}
.fax-title{position:absolute;right:26px;top:54px;font-size:11px;font-weight:700;font-style:normal;color:var(--brand-blue)}
.fax-head-addr{position:absolute;right:26px;top:22px;text-align:right}
.fax-fields{position:absolute;left:26px;right:26px;top:76px}
.fax-row{display:flex;gap:10px;margin-bottom:9px}
.fax-field{flex:1;display:flex;align-items:flex-end;gap:4px;font-size:5.5px;color:var(--ink)}
.fax-field span.fill{flex:1;border-bottom:1px solid var(--rule);height:7px}
.fax-checks{display:flex;justify-content:space-between;margin-top:4px;font-size:5px}
.fax-checks label{display:flex;align-items:center;gap:2px}
.box{width:5px;height:5px;border:1px solid var(--ink-soft);display:inline-block}
.fax-comments{font-size:5.5px;margin-top:14px}

/* business cards, right */
.wide-card{left:888px;width:264px;height:76px;padding:10px 14px}
.wide-card .logo{position:absolute;left:14px;top:28px}
.wide-card .contact{position:absolute;left:130px;top:16px}
.wide-card .side{position:absolute;right:12px;top:16px}
.wide-white{top:306px}
.wide-blue{top:392px;background:var(--brand-blue)}
.wide-blue .name,.wide-blue .fine{color:#fff}
.wide-bottom{top:492px;height:84px}
.wide-bottom .logo{top:auto;bottom:14px;left:auto;right:14px}
.wide-bottom .contact{left:14px;top:12px}

/* CD */
.cd-case{left:60px;top:620px;width:228px;height:184px;padding:14px}
.cd-case .addr{position:absolute;left:14px;top:70px}
.cd-case .web{position:absolute;left:0;right:0;bottom:8px;text-align:center}
.cd-disc{position:absolute;left:288px;top:636px;width:150px;height:150px}

/* cards bottom */
.note-blank{left:398px;top:614px;width:214px;height:190px}
.note-thanks{left:638px;top:614px;width:226px;height:190px}
.note-thanks .logo{position:absolute;left:50%;top:44px;transform:translateX(-50%)}
.note-thanks .logo-name{font-size:15px}
.thanks{position:absolute;left:0;right:0;top:120px;text-align:center;font-size:24px;color:var(--brand-blue)}
.holiday{left:888px;top:614px;width:288px;height:190px}
.holiday .photo{position:absolute;inset:0;background:linear-gradient(135deg,#c0301f 0%,#e9c56a 45%,#f6f0e4 70%,#2f6b2a 100%)}
.holiday .logo{position:absolute;right:14px;bottom:14px;background:rgba(255,255,255,.85);padding:3px 6px}
</style>
</head>
<body>

<section class="piece card-list" aria-label="Business card back">
  <div class="logo small"><span class="logo-dot"></span><span class="logo-name">VEXTORIAN</span></div>
  <div class="line"></div><div class="line"></div><div class="line"></div>
  <div class="line"></div><div class="line"></div><div class="line"></div>
</section>

<section class="piece card-front" aria-label="Business card front">
  <div class="logo"><span class="logo-dot"></span><span class="logo-name">VEXTORIAN</span></div>
  <div class="addr fine">9 Brindle Way, Suite 305<br>Toronto ON K7R4B9<br>Canada</div>
  <div class="contact">
    <div class="name">Luc-Henri Dorsay</div>
    <div class="fine">Senior Executive Consultant<br>T 416-555-0142<br>F 416-555-0143<br>luc-henri.dorsay@vextorian.example</div>
  </div>
  <div class="web fine">www.vextorian.example</div>
</section>

<section class="piece card-blue" aria-label="Business card services">
  <div class="heading">Business Consulting and Professional Services Portfolio</div>
  <ul>
    <li>eHealth consulting and research</li>
    <li>Healthcare IT project management</li>
    <li>Biomedical and health informatics</li>
    <li>Hospital and clinical engineering</li>
    <li>Business analysis and management</li>
    <li>Clean energy and technology management</li>
    <li>eLearning and knowledge translation</li>
  </ul>
  <div class="logo on-blue"><span class="logo-dot"></span><span class="logo-name">VEXTORIAN</span></div>
</section>

<section class="piece envelope env-back" aria-label="Envelope back"><div class="flap"></div></section>
<section class="piece envelope env-front" aria-label="Envelope front">
  <div class="flap"></div>
  <div class="logo small"><span class="logo-dot"></span><span class="logo-name">VEXTORIAN</span></div>
  <div class="window"></div>
</section>

<section class="piece sheet letterhead" aria-label="Letterhead">
  <div class="logo"><span class="logo-dot"></span><span class="logo-name">VEXTORIAN</span></div>
  <div class="sheet-rule"></div>
  <div class="sheet-foot fine">9 Brindle Way, Suite 305 · Toronto ON K7R4B9 · T 416-555-0142 · www.vextorian.example</div>
</section>

<section class="piece sheet fax" aria-label="Fax cover sheet">
  <div class="logo"><span class="logo-dot"></span><span class="logo-name">VEXTORIAN</span></div>
  <div class="fax-head-addr fine">9 Brindle Way, Suite 305<br>Toronto ON K7R4B9<br>Canada</div>
  <div class="fax-title">Fax Sheet</div>
  <div class="fax-fields">
    <div class="fax-row"><div class="fax-field">To:<span class="fill"></span></div><div class="fax-field">From:<span class="fill"></span></div></div>
    <div class="fax-row"><div class="fax-field">Fax:<span class="fill"></span></div><div class="fax-field">Pages:<span class="fill"></span></div></div>
    <div class="fax-row"><div class="fax-field">Phone:<span class="fill"></span></div><div class="fax-field">Date:<span class="fill"></span></div></div>
    <div class="fax-row"><div class="fax-field">Re:<span class="fill"></span></div><div class="fax-field">CC:<span class="fill"></span></div></div>
    <div class="fax-checks">
      <label><span class="box"></span>Urgent</label>
      <label><span class="box"></span>For Review</label>
      <label><span class="box"></span>Please Comment</label>
      <label><span class="box"></span>Please Reply</label>
      <label><span class="box"></span>Please Recycle</label>
    </div>
    <div class="fax-comments">Comments:</div>
  </div>
  <div class="sheet-rule"></div>
  <div class="sheet-foot fine">T 416-555-0142 · F 416-555-0143 · www.vextorian.example</div>
</section>

<section class="piece wide-card wide-white" aria-label="Business card">
  <div class="logo small"><span class="logo-dot"></span><span class="logo-name">VEXTORIAN</span></div>
  <div class="contact"><div class="name">Luc-Henri Dorsay</div><div class="fine">Senior Executive Consultant<br>luc-henri.dorsay@vextorian.example</div></div>
  <div class="side fine">T 416-555-0142<br>F 416-555-0143</div>
</section>

<section class="piece wide-card wide-blue" aria-label="Business card blue">
  <div class="logo small on-blue"><span class="logo-dot"></span><span class="logo-name">VEXTORIAN</span></div>
  <div class="contact"><div class="name">Luc-Henri Dorsay</div><div class="fine">Senior Executive Consultant<br>luc-henri.dorsay@vextorian.example</div></div>
  <div class="side fine">T 416-555-0142<br>F 416-555-0143</div>
</section>

<section class="piece wide-card wide-bottom" aria-label="Compliments card">
  <div class="contact"><div class="name">Luc-Henri Dorsay</div><div class="fine">9 Brindle Way, Suite 305<br>Toronto ON K7R4B9</div></div>
  <div class="logo small"><span class="logo-dot"></span><span class="logo-name">VEXTORIAN</span></div>
</section>

<section class="piece cd-case" aria-label="CD case cover">
  <div class="logo"><span class="logo-dot"></span><span class="logo-name">VEXTORIAN</span></div>
  <div class="addr fine">9 Brindle Way, Suite 305<br>Toronto ON K7R4B9<br>T 416-555-0142</div>
  <div class="web fine">www.vextorian.example</div>
</section>

<svg class="cd-disc" viewBox="0 0 150 150" aria-label="CD label">
  <circle cx="75" cy="75" r="73" fill="#fff" stroke="#d4d4d4"/>
  <circle cx="75" cy="75" r="22" fill="#eeeeee" stroke="#cfcfcf"/>
  <circle cx="75" cy="75" r="8" fill="var(--bg)" stroke="#bdbdbd"/>
  <circle cx="40" cy="40" r="3" fill="#7dbb3c"/>
  <text x="46" y="43" font-family="Open Sans, Arial, sans-serif" font-weight="700" font-size="9" fill="#2d6cc0" letter-spacing=".6">VEXTORIAN</text>
</svg>

<section class="piece note-blank" aria-label="Note card back"></section>

<section class="piece note-thanks" aria-label="Thank you card">
  <div class="logo"><span class="logo-dot"></span><span class="logo-name">VEXTORIAN</span></div>
  <div class="thanks">Thank You!</div>
</section>

<section class="piece holiday" aria-label="Holiday greeting card">
  <div class="photo" role="img" aria-label="Holiday photo of a candle with red ornaments and pine branches"></div>
  <div class="logo small"><span class="logo-dot"></span><span class="logo-name">VEXTORIAN</span></div>
</section>

</body>
</html>
```